RQT Livestock needs Buisness Card design using new logo

We need a business card design that ties our website and our new logo together. www.rqtlivestock-example.com The logo will be added to our website at a later date and replace the existing rqt livestock that is on the webpage. We are looking for a simple & professional design.

Target Market(s)

Cattle Producers, Ranchers

Industry/Entity Type

Agriculture

Contact Information for Business Card

Side one:
logo
www.rqtlivestock-example.com

Side two:
RQT Livestock
Robert & Tanya Quill
Fernvale, MB Canada
(555) 318-2094/(555) 627-4185
quill47@fernwire-example.net

Font styles to use
Serif
Sans Serif
Script

Requirements
Must have
• We would like to tie our new logo in with our website on the business card.

```html
<!DOCTYPE html>
<html lang="en">
<head>
<meta charset="utf-8">
<title>RQT Livestock – Business Card</title>
<link rel="stylesheet" href="https://fonts.googleapis.com/css2?family=Source+Sans+3:wght@400;600&display=swap">
<style>
  :root {
    --page-bg: #e6e8e7;
    --card-bg: #ffffff;
    --ink: #1c1c1c;
    --ink-soft: #3a3a3a;
    --accent: #d9341f;
    --decor: #ececec;
    --decor-deep: #e2e2e2;
  }
  * { box-sizing: border-box; margin: 0; padding: 0; }
  html, body {
    width: 1200px; height: 900px; overflow: hidden;
    background: var(--page-bg);
    font-family: "Source Sans 3", "Helvetica Neue", Arial, sans-serif;
    color: var(--ink);
  }
  .sheet {
    width: 1200px; height: 900px;
    display: flex; align-items: center; justify-content: center; gap: 40px;
  }
  .card {
    position: relative;
    width: 540px; height: 309px;
    background: var(--card-bg);
    box-shadow: 0 10px 26px rgba(0,0,0,.12), 0 2px 4px rgba(0,0,0,.06);
    overflow: hidden;
  }
  .card-decor {
    position: absolute; top: 0; right: 0; width: 150px; height: 100%;
    background: linear-gradient(100deg, rgba(236,236,236,0) 0%, var(--decor) 45%, var(--decor-deep) 100%);
  }
  .card-decor--low {
    top: auto; right: auto; left: 0; bottom: 0; width: 180px; height: 70px;
    background: linear-gradient(20deg, var(--decor-deep) 0%, rgba(236,236,236,0) 80%);
  }
  .brand {
    position: absolute; display: flex; align-items: center; gap: 10px;
    font-weight: 600; color: var(--ink); white-space: nowrap;
  }
  .brand-dot { width: 12px; height: 12px; border-radius: 50%; background: var(--accent); flex: none; }

  /* front */
  .card--front .brand { left: 150px; top: 112px; font-size: 40px; }
  .front-web {
    position: absolute; left: 0; right: 0; bottom: 70px; text-align: center;
    font-size: 13px; letter-spacing: 3px; color: var(--ink-soft);
  }

  /* back */
  .card--back .brand { left: 36px; top: 118px; font-size: 28px; }
  .holder { position: absolute; right: 48px; top: 58px; text-align: right; }
  .holder-name { font-size: 20px; font-weight: 600; }
  .holder-place { font-size: 11px; color: var(--ink-soft); margin-top: 2px; }
  .rule { position: absolute; left: 36px; right: 48px; top: 168px; height: 1px; background: var(--accent); }
  .contact { position: absolute; top: 190px; list-style: none; font-size: 13px; color: var(--ink-soft); }
  .contact li { display: flex; align-items: center; gap: 8px; line-height: 22px; }
  .contact svg { width: 11px; height: 11px; flex: none; }
  .contact--phones { left: 210px; }
  .contact--online { left: 345px; }
</style>
</head>
<body>
<main class="sheet">
  <section class="card card--front" aria-label="Card front">
    <div class="card-decor" role="img" aria-label="Faint grey leaf pattern along the edge"></div>
    <div class="card-decor card-decor--low" role="img" aria-label="Faint grey leaf pattern in the corner"></div>
    <div class="brand"><span class="brand-dot"></span>RQT Livestock</div>
    <p class="front-web">www.rqtlivestock-example.com</p>
  </section>

  <section class="card card--back" aria-label="Card back">
    <div class="card-decor" role="img" aria-label="Faint grey leaf pattern along the edge"></div>
    <div class="card-decor card-decor--low" role="img" aria-label="Faint grey leaf pattern in the corner"></div>
    <div class="brand"><span class="brand-dot"></span>RQT Livestock</div>
    <div class="holder">
      <p class="holder-name">Robert &amp; Tanya Quill</p>
      <p class="holder-place">Fernvale, MB Canada</p>
    </div>
    <div class="rule"></div>
    <ul class="contact contact--phones">
      <li><svg viewBox="0 0 10 10"><rect x="2" y="0.5" width="6" height="9" rx="1.2" fill="#d9341f"/><rect x="3.2" y="2" width="3.6" height="4.5" fill="#fff"/></svg>(555) 318-2094</li>
      <li><svg viewBox="0 0 10 10"><rect x="2" y="0.5" width="6" height="9" rx="1.2" fill="#d9341f"/><rect x="3.2" y="2" width="3.6" height="4.5" fill="#fff"/></svg>(555) 627-4185</li>
    </ul>
    <ul class="contact contact--online">
      <li><svg viewBox="0 0 10 10"><circle cx="5" cy="5" r="4.5" fill="#d9341f"/><circle cx="5" cy="5" r="1.8" fill="none" stroke="#fff" stroke-width="1"/></svg>quill47@fernwire-example.net</li>
      <li><svg viewBox="0 0 10 10"><rect x="0.5" y="2" width="9" height="6.5" fill="#d9341f"/><path d="M0.8 2.3 L5 5.6 L9.2 2.3" fill="none" stroke="#fff" stroke-width="0.9"/></svg>www.rqtlivestock-example.com</li>
    </ul>
  </section>
</main>
</body>
</html>
```